Veloran Dental Development - Business Cards

We are a Dental Development and Management company. We are looking to develop a new business card design. We are business professional but modern. The logo that I have attached is the business colors. You can also check out our website for further detail. www.veloranmgmt-example.com

Target Market(s)

Dental Professionals, Dentists and Office Staff, Marketing Professionals

Industry/Entity Type

Business

Requirements
Must have
• Name - Bartholomew K. Tressing
Title - Marketing Director
Phone - 555-019-4827
Cell - 555-019-4827
Email - Bart.t@veloran-example.com
Address - 2917 W Larkmoor Rd, Mesa, AZ 85209
Web- www.veloran-example.com

Veloran Logo must go on the front. The other logos go on the back as affiliated businesses

Must be editable to enter specific Names, Positions, Phone numbers and email later on. Using Adobe CS5 currently.

```html
<!DOCTYPE html>
<html lang="en">
<head>
<meta charset="utf-8">
<title>Veloran Dental Development – Business Cards</title>
<link href="https://fonts.googleapis.com/css2?family=Open+Sans:wght@400;600;700&display=swap" rel="stylesheet">
<style>
  :root {
    --navy: #2c336f;
    --navy-deep: #232a5e;
    --gold: #e3a444;
    --white: #ffffff;
    --paper: #f4f4f4;
    --ink-grey: #555555;
    --stage-top: #8a8a8a;
    --stage-bottom: #f2f2f2;
  }
  * { box-sizing: border-box; margin: 0; padding: 0; }
  html, body { width: 1200px; height: 861px; overflow: hidden; }
  body {
    font-family: "Open Sans", Arial, sans-serif;
    background: linear-gradient(to bottom, var(--stage-top) 0%, #c9c9c9 40%, var(--stage-bottom) 75%, var(--white) 100%);
    position: relative;
  }
  .card {
    position: absolute;
    top: 260px;
    width: 520px;
    height: 310px;
    overflow: hidden;
    box-shadow: 0 8px 22px rgba(0,0,0,0.25);
  }
  /* Back of card */
  .card-back { left: 60px; background: var(--navy); }
  .card-back .brand {
    position: absolute; top: 62px; left: 0; right: 0;
    text-align: center; color: var(--white);
    font-weight: 600; font-size: 34px; letter-spacing: 2px; line-height: 1.2;
  }
  .card-back .brand small { display: block; font-size: 17px; letter-spacing: 3px; }
  .card-back .website {
    position: absolute; top: 160px; left: 0; right: 0;
    text-align: center; color: var(--white); font-size: 17px;
  }
  .affiliates {
    position: absolute; top: 210px; left: 0; right: 0; height: 74px;
    background: var(--white); text-align: center;
  }
  .affiliates-title { color: var(--gold); font-size: 9px; padding-top: 8px; }
  .affiliate-row {
    display: flex; justify-content: center; align-items: center;
    gap: 18px; margin-top: 14px;
  }
  .affiliate {
    color: var(--navy); font-size: 9px; font-weight: 700; line-height: 1.1; text-align: center;
  }
  .affiliate-badge { width: 34px; height: 34px; border-radius: 50%; background: var(--gold); }

  /* Front of card */
  .card-front { left: 620px; background: radial-gradient(circle at 50% 40%, var(--white), var(--paper)); }
  .card-front .brand {
    position: absolute; top: 48px; left: 0; right: 0;
    text-align: center; color: var(--navy);
    font-weight: 600; font-size: 30px; letter-spacing: 2px; line-height: 1.2;
  }
  .card-front .brand small { display: block; font-size: 15px; letter-spacing: 3px; }
  .person-name {
    position: absolute; top: 140px; left: 0; right: 0; text-align: center;
    color: var(--navy); font-size: 27px; font-weight: 700;
  }
  .person-title {
    position: absolute; top: 178px; left: 0; right: 0; text-align: center;
    color: var(--ink-grey); font-size: 15px; font-weight: 600;
  }
  .contact-band {
    position: absolute; top: 210px; left: 0; right: 0; height: 80px;
    background: var(--gold);
  }
  .contact-panel {
    position: absolute; top: 0; bottom: 0; left: 92px; right: 92px;
    background: var(--navy); color: var(--white); font-size: 12px;
  }
  .address { position: absolute; top: 8px; left: 0; right: 0; text-align: center; }
  .phones { position: absolute; top: 40px; left: 8px; line-height: 18px; font-size: 13px; }
  .online { position: absolute; top: 34px; right: 8px; text-align: right; line-height: 17px; }
  .icons-left, .icons-right {
    position: absolute; top: 36px; display: flex; flex-direction: column; gap: 6px;
  }
  .icons-left { left: 70px; }
  .icons-right { right: 76px; }
</style>
</head>
<body>
  <section class="card card-back">
    <div class="brand">Veloran<small>Dental Development</small></div>
    <div class="website">www.veloran-example.com</div>
    <div class="affiliates">
      <div class="affiliates-title">Affiliated Businesses</div>
      <div class="affiliate-row">
        <div class="affiliate">Hearthside<br>Dental Centers</div>
        <div class="affiliate">Hearthside<br>Dental Plan</div>
        <div class="affiliate">Rapidcare<br>Dental Centers</div>
        <div class="affiliate-badge" role="img" aria-label="Affiliate badge"></div>
      </div>
    </div>
  </section>

  <section class="card card-front">
    <div class="brand">Veloran<small>Dental Development</small></div>
    <div class="person-name">Bartholomew K. Tressing</div>
    <div class="person-title">Marketing Director</div>
    <div class="contact-band">
      <div class="icons-left">
        <svg width="12" height="14" viewBox="0 0 12 14" aria-label="Phone"><path d="M2 1h3l1 3-2 1q1 3 4 4l1-2 3 1v3q-1 1-3 1Q2 11 1 3q0-2 1-2z" fill="#fff"/></svg>
        <svg width="10" height="14" viewBox="0 0 10 14" aria-label="Mobile"><rect x="1" y="0.5" width="8" height="13" rx="1.5" fill="none" stroke="#fff"/><rect x="2.5" y="2" width="5" height="7" fill="#fff"/></svg>
      </div>
      <div class="contact-panel">
        <div class="address">2917 W Larkmoor Rd, Mesa, AZ 85209</div>
        <div class="phones">555.019.4827<br>555.019.4827</div>
        <div class="online">Bart.t@veloran-example.com<br>www.veloran-example.com</div>
      </div>
      <div class="icons-right">
        <svg width="13" height="10" viewBox="0 0 13 10" aria-label="Email"><rect x="0.5" y="0.5" width="12" height="9" fill="none" stroke="#fff"/><path d="M0.5 0.5l6 5 6-5" fill="none" stroke="#fff"/></svg>
        <svg width="13" height="10" viewBox="0 0 13 10" aria-label="Website"><rect x="0.5" y="0.5" width="12" height="9" fill="none" stroke="#fff"/><rect x="0.5" y="0.5" width="12" height="2.5" fill="#fff"/></svg>
      </div>
    </div>
  </section>
</body>
</html>
```